Letterhead and Business Card for Wealth Management Company
Harborline Wealth Management
Letterhead and Business Card for Wealth Management Company - Financial Services
Creative Brief
Use same font as used in my logo
Can use the same font or add additional font
Professional
R. Dwight Voss, CRPC®
Wealth Advisor
2450 Fernbrook Avenue Suite 310 Berwyn, PA 19312
dvoss@harborline-wealth.com
www.harborline-wealth.com
I work with affluent people so I want a sophisticated and classic looking business card and stationary. Our tagline is Dream. Plan. Live. with Live in italics. You can see it on our website at www.harborline-wealth.com. If appropriate, please include the tagline on the business card, letterhead and envelope. Please note the tagline on the website is a gradient color. It looks better printed in solid color.
Be creative.
dvoss dvoss
Thanks for all the great designs! I have a busy schedule today, but I will go through them and give star ratings later today or tonight. Thanks again!
Qwirk Qwirk

```html
<!DOCTYPE html>
<html lang="en">
<head>
<meta charset="utf-8">
<title>Harborline Wealth Management – Business Card</title>
<link href="https://fonts.googleapis.com/css2?family=Cinzel:wght@600&family=Open+Sans:wght@400;600;700&display=swap" rel="stylesheet">
<style>
  :root {
    --backdrop: #d9dadc;
    --paper: #ffffff;
    --navy: #1d3a6e;
    --gold: #c9a24a;
    --silver: #c3c7cf;
    --ink: #1d3a6e;
    --white: #ffffff;
  }
  * { box-sizing: border-box; margin: 0; padding: 0; }
  html, body { width: 1200px; height: 902px; overflow: hidden; }
  body {
    background: var(--backdrop);
    position: relative;
    font-family: "Open Sans", Arial, sans-serif;
  }
  .card {
    position: absolute;
    left: 270px;
    width: 660px;
    height: 377px;
    background: var(--paper);
    box-shadow: 0 6px 18px rgba(0,0,0,0.18);
    overflow: hidden;
  }
  .card--front { top: 44px; }
  .card--back { top: 481px; }

  .brand {
    position: absolute;
    display: flex;
    align-items: center;
    gap: 14px;
  }
  .brand__mark {
    width: 34px; height: 34px;
    background: var(--gold);
    flex: none;
  }
  .brand__name {
    font-family: "Cinzel", Georgia, serif;
    font-weight: 600;
    color: var(--navy);
    line-height: 1.05;
  }
  .card--front .brand { left: 0; right: 0; top: 140px; justify-content: center; }
  .card--front .brand__name { font-size: 30px; }
  .card--front .brand__mark { width: 48px; height: 48px; }

  .card--back .brand { left: 46px; top: 70px; }
  .card--back .brand__name { font-size: 21px; }

  .holder {
    position: absolute;
    left: 62px;
    top: 262px;
    color: var(--ink);
  }
  .holder__name { font-size: 17px; font-weight: 700; }
  .holder__title { font-size: 14px; margin-top: 2px; }

  .wave { position: absolute; inset: 0; width: 100%; height: 100%; }
  .wave .panel { fill: var(--navy); }
  .wave .stripe-gold { fill: none; stroke: var(--gold); stroke-width: 4; }
  .wave .stripe-silver { fill: none; stroke: var(--silver); stroke-width: 9; }

  .contact {
    position: absolute;
    right: 30px;
    top: 128px;
    list-style: none;
    text-align: right;
    color: var(--white);
    font-size: 11.5px;
    line-height: 18px;
  }
  .contact li { display: flex; justify-content: flex-end; align-items: center; gap: 7px; }
  .contact svg { width: 11px; height: 11px; fill: var(--white); flex: none; }
  .contact .gap { margin-top: 6px; }
</style>
</head>
<body>

  <section class="card card--front" aria-label="Business card front">
    <div class="brand">
      <span class="brand__mark"></span>
      <span class="brand__name">Harborline<br>Wealth Management</span>
    </div>
  </section>

  <section class="card card--back" aria-label="Business card back">
    <svg class="wave" viewBox="0 0 660 377" preserveAspectRatio="none" aria-hidden="true">
      <path class="stripe-silver" d="M120 377 C 270 335, 285 150, 410 90 C 510 42, 600 48, 660 33"/>
      <path class="panel" d="M185 377 C 320 340, 335 170, 452 110 C 540 66, 610 70, 660 55 L660 377 Z"/>
      <path class="stripe-gold" d="M150 377 C 296 338, 310 160, 431 100 C 525 54, 605 59, 660 44"/>
    </svg>

    <div class="brand">
      <span class="brand__mark"></span>
      <span class="brand__name">Harborline<br>Wealth Management</span>
    </div>

    <div class="holder">
      <p class="holder__name">Maren Holt-Pryce</p>
      <p class="holder__title">Consultant</p>
    </div>

    <ul class="contact">
      <li>2450 Fernbrook Avenue</li>
      <li>Berwyn, PA 19312
        <svg viewBox="0 0 12 12"><path d="M6 0a4 4 0 0 0-4 4c0 3 4 8 4 8s4-5 4-8a4 4 0 0 0-4-4zm0 5.5A1.5 1.5 0 1 1 6 2.5a1.5 1.5 0 0 1 0 3z"/></svg>
      </li>
      <li class="gap">610 555 0142
        <svg viewBox="0 0 12 12"><path d="M2.5 0.5l2 2.5-1.2 1.3a7 7 0 0 0 4.4 4.4L9 7.5l2.5 2L10 11.5C5 11.5 0.5 7 0.5 2z"/></svg>
      </li>
      <li>dvoss@harborline-wealth.com
        <svg viewBox="0 0 12 12"><path d="M0 2h12v8H0zM1 3v.4l5 3.2 5-3.2V3z"/></svg>
      </li>
      <li>www.harborline-wealth.com</li>
    </ul>
  </section>

</body>
</html>
```